Brochure for Community-Based Therapy Company

Will be given out to patients, doctors, case managers. We are redesigning our marketing materials and would like a design for a brochure. We provide therapy to individuals who have been injured in car accidents or on the job. We provide occupational therapy, speech therapy and psychotherapy. We would like the brochure to utilize our corporate ID and color scheme that we are using for our other materials (see attached letterhead and logo).

Stock photos that are used should stay away from images of outpatient or hospital settings, stay away from photos with obvious disabilities (wheelchairs, learning to walk, etc), and nothing that looks like physical therapy, as we don't provide physical therapy only OT, Speech and psychotherapy. Would prefer to not have people wearing masks, as we will use this beyond the pandemic. Also, our staff wears business casual clothing so would prefer photos that the individuals are not wearing scrubs or other medical attire (lab coats, etc).

Target Market(s)

Patients, Physicians/Doctors, Case Managers

Industry/Entity Type

Healthcare

Requirements
Must have
• Prefer a booklet format but doesn't have to be 8.5 inch by 11 inch (can be a little smaller).

```html
<!DOCTYPE html>
<html lang="en">
<head>
<meta charset="utf-8">
<title>Northbrook Recovery Services – Tri-fold Brochure</title>
<link href="https://fonts.googleapis.com/css2?family=Open+Sans:wght@400;600;700;800&display=swap" rel="stylesheet">
<style>
  :root {
    --sage: #7ea596;
    --sage-dark: #5b8676;
    --sage-deep: #3f6a5c;
    --sage-light: #dde8e3;
    --sage-mist: #eef3f1;
    --paper: #ffffff;
    --ink: #4a4f4d;
    --ink-soft: #6b716e;
    --backdrop: #d9dbdb;
    --photo-a: #b9c4bf;
    --photo-b: #8e9c95;
  }
  * { box-sizing: border-box; margin: 0; padding: 0; }
  html, body { width: 1200px; height: 2400px; overflow: hidden; }
  body {
    background: var(--backdrop);
    font-family: "Open Sans", Arial, sans-serif;
    color: var(--ink);
    position: relative;
  }
  .spread {
    position: absolute;
    left: 60px;
    width: 1080px;
    height: 835px;
    display: flex;
    box-shadow: 0 10px 30px rgba(0,0,0,.18);
  }
  .spread--outside { top: 243px; }
  .spread--inside { top: 1321px; }
  .panel {
    position: relative;
    width: 360px;
    height: 835px;
    overflow: hidden;
    background: var(--paper);
  }
  .panel + .panel { border-left: 1px solid rgba(0,0,0,.06); }
  .panel-shapes { position: absolute; inset: 0; width: 100%; height: 100%; }
  .photo {
    position: absolute;
    background: linear-gradient(135deg, var(--photo-a), var(--photo-b));
  }
  .photo--round {
    border-radius: 50%;
    border: 5px solid var(--paper);
    box-shadow: 0 2px 6px rgba(0,0,0,.2);
  }
  .brand {
    position: absolute;
    display: flex;
    align-items: center;
    gap: 8px;
    font-weight: 700;
    color: var(--sage-dark);
    text-transform: uppercase;
    letter-spacing: .5px;
    line-height: 1.15;
  }
  .brand-dot {
    flex: none;
    width: 14px; height: 14px;
    border-radius: 50%;
    background: var(--sage);
  }
  .heading {
    font-weight: 800;
    color: var(--sage-dark);
    text-transform: uppercase;
    line-height: 1.15;
  }
  .body-text { font-size: 10.5px; line-height: 1.6; color: var(--ink); }
  .body-text p { margin-bottom: 9px; }
  .subhead { font-size: 11.5px; font-weight: 700; color: var(--sage-dark); margin: 8px 0 6px; }
  .list { list-style: none; }
  .list li {
    position: relative;
    padding-left: 14px;
    margin-bottom: 5px;
    font-size: 10.5px;
    line-height: 1.5;
  }
  .list li::before {
    content: "";
    position: absolute;
    left: 0; top: 6px;
    width: 6px; height: 6px;
    border-radius: 50%;
    background: var(--sage);
  }
  .band-text {
    position: absolute;
    color: var(--paper);
    text-align: center;
  }

  /* outside: about flap */
  .about .photo--round { left: 26px; top: 22px; width: 104px; height: 104px; }
  .about .heading { position: absolute; left: 150px; right: 24px; top: 150px; font-size: 17px; text-align: right; }
  .about .body-text { position: absolute; left: 30px; right: 30px; top: 215px; }
  .about .website { bottom: 34px; left: 0; right: 0; font-size: 11px; }

  /* outside: contact */
  .contact { background: var(--sage-mist); }
  .contact .photo--top { left: 0; top: 0; width: 360px; height: 240px; }
  .contact .brand { left: 60px; right: 40px; top: 285px; font-size: 15px; }
  .contact .details { position: absolute; left: 30px; right: 30px; top: 370px; text-align: center; }
  .contact .details .heading { font-size: 19px; margin-bottom: 14px; }
  .contact .details p { font-size: 12px; line-height: 1.55; margin-bottom: 12px; color: var(--ink); }
  .contact .details .phone { font-size: 15px; font-weight: 700; color: var(--sage-deep); }
  .contact .band-text { left: 30px; right: 30px; bottom: 36px; font-size: 11.5px; line-height: 1.55; }

  /* outside: cover */
  .cover .brand { left: 110px; right: 20px; top: 38px; font-size: 16px; }
  .cover .photo--hero { left: 0; top: 120px; width: 360px; height: 500px; }
  .cover .band-text { left: 22px; right: 22px; top: 650px; }
  .cover .tagline { font-size: 17px; font-weight: 700; line-height: 1.35; margin-bottom: 12px; }
  .cover .band-text p:last-child { font-size: 10.5px; line-height: 1.55; opacity: .95; }

  /* inside */
  .inside-panel .heading { position: absolute; font-size: 19px; }
  .speech .heading { left: 30px; top: 92px; }
  .speech .body-text { position: absolute; left: 30px; right: 28px; top: 150px; }
  .ot .photo--top { left: 0; top: 0; width: 360px; height: 200px; }
  .ot .heading { left: 0; right: 0; top: 222px; text-align: center; }
  .ot .body-text { position: absolute; left: 30px; right: 28px; top: 262px; }
  .psych .photo--round { right: 24px; top: 14px; width: 96px; height: 96px; }
  .psych .heading { left: 30px; right: 30px; top: 118px; }
  .psych .body-text { position: absolute; left: 30px; right: 28px; top: 170px; }
</style>
</head>
<body>

<!-- Outside spread -->
<section class="spread spread--outside">

  <article class="panel about">
    <svg class="panel-shapes" viewBox="0 0 360 835" preserveAspectRatio="none" aria-hidden="true">
      <path d="M0 0 H360 V24 C250 40 170 110 0 150 Z" fill="var(--sage)"/>
      <path d="M0 160 C170 118 250 48 360 34" stroke="var(--sage-light)" stroke-width="3" fill="none"/>
      <path d="M0 760 C120 730 240 738 360 700 V835 H0 Z" fill="var(--sage)"/>
      <path d="M0 748 C120 718 240 726 360 688" stroke="var(--sage-light)" stroke-width="3" fill="none"/>
    </svg>
    <div class="photo photo--round" role="img" aria-label="Therapist chatting with a client at home"></div>
    <h2 class="heading">Northbrook Recovery Services</h2>
    <div class="body-text">
      <p>We are a community based team that supports people recovering from auto and work injuries across the region.</p>
      <p>Our therapists meet clients at home, at work and in the community, building skills for real daily life and lasting independence.</p>
      <div class="subhead">Services</div>
      <ul class="list">
        <li>Speech Language Pathology</li>
        <li>Occupational Therapy</li>
        <li>Psychological Counseling</li>
        <li>Cognitive Rehabilitation</li>
        <li>Case Management Support</li>
        <li>Community Reintegration</li>
        <li>Return to Work Planning</li>
        <li>Family Education</li>
      </ul>
    </div>
    <p class="band-text website">www.northbrookrecovery.com</p>
  </article>

  <article class="panel contact">
    <div class="photo photo--top" role="img" aria-label="Therapist working with a client on a daily living task"></div>
    <svg class="panel-shapes" viewBox="0 0 360 835" preserveAspectRatio="none" aria-hidden="true">
      <path d="M0 200 C110 250 250 250 360 190 V260 H0 Z" fill="var(--sage-mist)"/>
      <path d="M0 196 C110 246 250 246 360 186" stroke="var(--sage)" stroke-width="5" fill="none"/>
      <path d="M0 720 C120 690 240 700 360 660 V835 H0 Z" fill="var(--sage)"/>
      <path d="M0 708 C120 678 240 688 360 648" stroke="var(--paper)" stroke-width="2" fill="none" opacity=".7"/>
    </svg>
    <div class="brand"><span class="brand-dot"></span><span>Northbrook Recovery Services Inc.</span></div>
    <div class="details">
      <h2 class="heading">Contact Us</h2>
      <p>4820 Meadow Ridge Drive, Suite 210<br>Lakeview, MI 48000</p>
      <p class="phone">555-014-2290</p>
      <p>Office Hours: Monday – Friday 9:00 am – 5:00 pm<br>Therapy Hours: By Appointment</p>
      <p>hello@northbrookrecovery.com<br>www.northbrookrecovery.com</p>
    </div>
    <p class="band-text">Please contact us at <strong>555-014-2290</strong> or <strong>hello@northbrookrecovery.com</strong> for more information on getting started.</p>
  </article>

  <article class="panel cover">
    <div class="brand"><span class="brand-dot"></span><span>Northbrook Recovery Services Inc.</span></div>
    <div class="photo photo--hero" role="img" aria-label="Smiling client in a knit scarf outdoors"></div>
    <svg class="panel-shapes" viewBox="0 0 360 835" preserveAspectRatio="none" aria-hidden="true">
      <path d="M0 640 C120 590 250 560 360 520 V835 H0 Z" fill="var(--sage)"/>
      <path d="M0 626 C120 576 250 546 360 506" stroke="var(--sage-light)" stroke-width="3" fill="none"/>
    </svg>
    <div class="band-text">
      <p class="tagline">This is our commitment to you,<br>Everyone Benefits – Everyone Wins</p>
      <p>We are a community based team helping people recover after injury, with goals set by each client and family.</p>
    </div>
  </article>
</section>

<!-- Inside spread -->
<section class="spread spread--inside">

  <article class="panel inside-panel speech">
    <svg class="panel-shapes" viewBox="0 0 360 835" preserveAspectRatio="none" aria-hidden="true">
      <path d="M0 0 H360 V20 C240 30 120 60 0 80 Z" fill="var(--sage)"/>
      <path d="M0 790 C120 775 240 770 360 760 V835 H0 Z" fill="var(--sage)"/>
    </svg>
    <h2 class="heading">Speech Language<br>Pathology</h2>
    <div class="body-text">
      <p>Speech language pathologists are trained to evaluate and treat disorders of language, speech, voice and swallowing. After an injury, these skills may change, and our therapists help each client rebuild clear communication for home, work and the wider community.</p>
      <div class="subhead">Services Include:</div>
      <ul class="list">
        <li>Attention and concentration training for daily tasks</li>
        <li>Expressive language: finding words and forming clear sentences</li>
        <li>Comprehension of spoken and written information</li>
        <li>Memory strategies for routines, notes and schedules</li>
        <li>Word retrieval and organized thought for speaking</li>
        <li>Pragmatic and social communication skills</li>
        <li>Executive function: planning, problem solving and self monitoring</li>
        <li>Articulation</li>
        <li>Dysphagia (swallowing disorders)</li>
        <li>Voice</li>
      </ul>
    </div>
  </article>

  <article class="panel inside-panel ot">
    <div class="photo photo--top" role="img" aria-label="Group of clients and therapist talking around a table"></div>
    <svg class="panel-shapes" viewBox="0 0 360 835" preserveAspectRatio="none" aria-hidden="true">
      <path d="M0 170 C120 215 240 215 360 170 V220 H0 Z" fill="var(--paper)"/>
      <path d="M0 166 C120 211 240 211 360 166" stroke="var(--sage)" stroke-width="4" fill="none"/>
      <path d="M0 760 C120 770 240 775 360 790 V835 H0 Z" fill="var(--sage)"/>
    </svg>
    <h2 class="heading">Occupational Therapy</h2>
    <div class="body-text">
      <p>Occupational therapists focus on the everyday activities that matter most to each person. We work in real settings so new skills carry over into home life, work and the community.</p>
      <div class="subhead">Services Include:</div>
      <ul class="list">
        <li>Getting around the community and using public transit safely and with confidence</li>
        <li>Building personal routines for self care, meals and household tasks</li>
        <li>Managing time, money, appointments and medications</li>
        <li>Evaluating home safety and recommending equipment</li>
        <li>Returning to work, school and volunteer roles</li>
        <li>Improving upper body strength and fine motor skills</li>
        <li>Addressing vision and perceptual challenges</li>
        <li>Supporting leisure and social participation</li>
        <li>Training families and caregivers in helpful strategies</li>
      </ul>
    </div>
  </article>

  <article class="panel inside-panel psych">
    <svg class="panel-shapes" viewBox="0 0 360 835" preserveAspectRatio="none" aria-hidden="true">
      <path d="M0 0 H360 V60 C250 40 120 20 0 30 Z" fill="var(--sage)"/>
      <path d="M0 790 C120 780 240 770 360 745 V835 H0 Z" fill="var(--sage)"/>
    </svg>
    <div class="photo photo--round" role="img" aria-label="Counselor meeting with a client"></div>
    <h2 class="heading">Psychological and Counseling</h2>
    <div class="body-text">
      <div class="subhead">Individual &amp; Family Counseling provided in-home and in the community:</div>
      <ul class="list">
        <li>Adjustment to injury and changes in life roles</li>
        <li>Anxiety, depression and mood management</li>
        <li>Stress, sleep and coping with chronic pain</li>
        <li>Trauma related to accidents and workplace events</li>
        <li>Family support and communication</li>
      </ul>
      <div class="subhead">Additional Services:</div>
      <ul class="list">
        <li>Neuropsychological testing and cognitive screening</li>
        <li>Behavior plans for home and community settings</li>
        <li>Coordination with physicians and case managers</li>
        <li>Referrals to community resources</li>
        <li>Goal setting and progress reports for the care team</li>
      </ul>
    </div>
  </article>
</section>

</body>
</html>
```